Home Multi-Service Company Website

I currently have only a landing page but am looking for someone to build out a nice, modern looking website that will cover multiple services we offer like Landscape Lighting, Gutter Cleaning, Holiday Lighting, Window Cleaning, Insulation Services like Blow In and Removal, Blower Door Tests, Rodent Exclusion and Trapping and others. We would also like our Holiday lighting category to have links to a separate page for franchise opportunities.

Target Market(s)

Home

Font styles to use
Serif
Sans Serif

Requirements
Must have
• A modern and organized look. Detailed information regarding each service provided by our company.
Nice to have
• We are a service company so would like to see options to link reviews from quorvel and maybe some nice pictures of people at home. We would like the color to match our logo as well.

```html
<!DOCTYPE html>
<html lang="en">
<head>
<meta charset="utf-8">
<title>Hearthwell Services</title>
<link href="https://fonts.googleapis.com/css2?family=Playfair+Display:ital,wght@1,700&family=EB+Garamond:wght@500&family=Poppins:wght@300;400;500;600&display=swap" rel="stylesheet">
<style>
:root{
  --slate:#47545e;
  --slate-dark:#3d4952;
  --ink:#1e1e1e;
  --body:#6b6b6b;
  --white:#ffffff;
  --field:#5b6770;
  --black:#111111;
  --navy:#2f3f63;
}
*{margin:0;padding:0;box-sizing:border-box}
html,body{width:1200px;height:4501px;overflow:hidden;background:var(--white)}
body{position:relative;font-family:"Poppins",sans-serif;color:var(--body)}
.abs{position:absolute}
.brand{font-family:"Poppins",sans-serif;font-weight:600;color:var(--slate);font-size:25px;display:flex;align-items:center;gap:10px;letter-spacing:.5px}
.brand .sq{width:18px;height:18px;background:currentColor}
.pill{display:flex;align-items:center;justify-content:center;border-radius:20px;font-weight:500;font-size:13px;letter-spacing:.3px;text-transform:uppercase}
.header-btn{left:975px;top:30px;width:164px;height:37px;background:var(--slate);color:var(--white)}
.hero{left:0;top:96px;width:1200px;height:638px;background:linear-gradient(90deg,#5a524a 0%,#8a7d70 45%,#6f6358 75%,#4a4039 100%)}
.hero-title{left:61px;top:318px;font-family:"Playfair Display",serif;font-style:italic;font-weight:700;font-size:58px;color:var(--white)}
.hero-text{left:61px;top:398px;width:410px;font-size:14px;line-height:21px;color:var(--white);font-weight:300}
.hero-btn{left:61px;top:484px;width:163px;height:37px;background:var(--white);color:var(--ink)}
.welcome{left:0;top:808px;width:1200px;text-align:center}
.welcome small{display:block;font-size:11px;color:var(--ink);font-weight:500}
.welcome h1{font-size:24px;font-weight:600;color:var(--ink);letter-spacing:.5px;margin-top:4px}
.welcome .rule{width:80px;height:2px;background:var(--navy);margin:6px auto 0}
.welcome p{width:550px;margin:18px auto 0;font-size:12.5px;line-height:19px;font-weight:300}
.service-photo{width:487px;height:337px}
.service-text{width:380px}
.service-text h2{font-family:"EB Garamond",serif;font-weight:500;font-size:24px;color:var(--ink);display:inline-block;border-bottom:2px solid var(--navy);padding-bottom:2px;line-height:28px}
.service-text p{font-size:12px;line-height:19.5px;font-weight:300;margin-top:18px}
.service-text p + p{margin-top:14px}
.band{left:0;top:3187px;width:1200px;height:337px;background:var(--slate)}
.band-photo{left:0;top:3187px;width:420px;height:337px}
.band-text{left:500px;top:3245px;width:380px;color:var(--white)}
.band-text h2{font-family:"EB Garamond",serif;font-weight:500;font-size:24px;display:inline-block;border-bottom:2px solid var(--white);padding-bottom:2px}
.band-text p{font-size:12px;line-height:19.5px;font-weight:300;margin-top:16px}
.band-text p + p{margin-top:10px}
.blow-title{left:0;top:3593px;width:1200px;text-align:center;font-size:24px;font-weight:600;color:var(--ink)}
.blow-title span{display:inline-block;border-bottom:2px solid var(--navy);padding:0 2px 3px;line-height:28px}
.card{top:3655px;width:262px;height:293px;background:var(--white);box-shadow:0 2px 10px rgba(0,0,0,.08)}
.card svg{display:block}
.card h3{font-size:15px;font-weight:400;color:var(--ink);margin:22px 0 0 24px}
.footer{left:0;top:4023px;width:1200px;height:441px;background:var(--slate)}
.footer-brand{left:0;top:4090px;width:1200px;justify-content:center;color:var(--white);font-size:34px}
.contact{top:4168px;display:flex;align-items:center;gap:14px;color:var(--white);font-size:12px;line-height:19px;font-weight:300}
.contact .ico{width:32px;height:32px;border-radius:50%;background:var(--white);display:flex;align-items:center;justify-content:center;flex:none}
.field{top:4237px;height:37px;border-radius:18px;background:var(--field);color:var(--white);font-size:12px;padding:10px 0 0 16px;font-weight:300}
.message{left:255px;top:4282px;width:689px;height:72px;border-radius:14px;background:var(--field);color:var(--white);font-size:12px;padding:22px 16px;font-weight:300}
.send{left:521px;top:4366px;width:89px;height:35px;background:var(--black);color:var(--white);font-size:13px}
.copyright{left:0;top:4464px;width:1200px;height:37px;background:var(--black);color:var(--white);font-size:11px;display:flex;align-items:center;justify-content:center;font-weight:300}
</style>
</head>
<body>

<header>
  <div class="abs brand" style="left:61px;top:30px"><span class="sq"></span>Hearthwell</div>
  <div class="abs pill header-btn">Holiday Lighting</div>
</header>

<section>
  <div class="abs hero" role="img" aria-label="Family relaxing together on a sofa in a bright living room"></div>
  <h1 class="abs hero-title">Hearthwell Service</h1>
  <p class="abs hero-text">Lorem Ipsum is simply dummy text of the printing and typesetting industry. Lorem Ipsum has been the industry's standard dummy text ever since the 1500s</p>
  <div class="abs pill hero-btn">Holiday Lighting</div>
</section>

<section class="abs welcome">
  <small>WELCOME TO</small>
  <h1>HEARTHWELL SERVICE</h1>
  <div class="rule"></div>
  <p>Lorem Ipsum is simply dummy text of the printing and typesetting industry. Lorem Ipsum has been the industry's standard dummy text ever since the 1500s, when an unknown printer took a galley of type and scrambled it to make a type specimen book.</p>
</section>

<div class="abs service-photo" style="left:60px;top:1008px;background:linear-gradient(180deg,#3b4a63 0%,#5a6478 40%,#3e4a2e 75%,#2f3b22 100%)" role="img" aria-label="White two-storey house with landscape lighting at dusk"></div>
<div class="abs service-text" style="left:673px;top:1046px">
  <h2>Landscape Lighting</h2>
  <p>Lorem Ipsum is simply dummy text of the printing and typesetting industry. Lorem Ipsum has been the industry's standard dummy text ever since the 1500s, when an unknown printer took a galley of type and scrambled it to make a type specimen book.</p>
  <p>It is a long established fact that a reader will be distracted by the readable content of a page when looking at its layout. The point of using Lorem Ipsum is that it has a more-or-less normal distribution of letters, as opposed to using 'Content here.</p>
</div>

<div class="abs service-photo" style="left:615px;top:1443px;background:linear-gradient(135deg,#7d7a74 0%,#6b6357 45%,#8a8680 100%)" role="img" aria-label="Gloved hand clearing leaves from a roof gutter"></div>
<div class="abs service-text" style="left:121px;top:1489px">
  <h2>Gutter Cleaning</h2>
  <p>Lorem Ipsum is simply dummy text of the printing and typesetting industry. Lorem Ipsum has been the industry's standard dummy text ever since the 1500s, when an unknown printer took a galley of type and scrambled it to make a type specimen book.</p>
  <p>It is a long established fact that a reader will be distracted by the readable content of a page when looking at its layout. The point of using Lorem Ipsum is that it has a more-or-less normal distribution of letters, as opposed to using 'Content here.</p>
</div>

<div class="abs service-photo" style="left:60px;top:1878px;background:radial-gradient(ellipse at 50% 55%,#a8683a 0%,#5a3018 45%,#1a0f0a 100%)" role="img" aria-label="House decorated with holiday lights at night"></div>
<div class="abs service-text" style="left:673px;top:1916px">
  <h2>Holiday Lighting</h2>
  <p>Lorem Ipsum is simply dummy text of the printing and typesetting industry. Lorem Ipsum has been the industry's standard dummy text ever since the 1500s, when an unknown printer took a galley of type and scrambled it to make a type specimen book.</p>
  <p>It is a long established fact that a reader will be distracted by the readable content of a page when looking at its layout. The point of using Lorem Ipsum is that it has a more-or-less normal distribution of letters, as opposed to using 'Content here.</p>
</div>

<div class="abs service-photo" style="left:615px;top:2313px;background:linear-gradient(90deg,#b8684a 0%,#c9876a 40%,#a5b5b2 75%,#b56a4e 100%)" role="img" aria-label="Woman cleaning a window on a brick wall"></div>
<div class="abs service-text" style="left:91px;top:2359px">
  <h2>Window Cleaning</h2>
  <p>Lorem Ipsum is simply dummy text of the printing and typesetting industry. Lorem Ipsum has been the industry's standard dummy text ever since the 1500s, when an unknown printer took a galley of type and scrambled it to make a type specimen book.</p>
  <p>It is a long established fact that a reader will be distracted by the readable content of a page when looking at its layout. The point of using Lorem Ipsum is that it has a more-or-less normal distribution of letters, as opposed to using 'Content here.</p>
</div>

<div class="abs service-photo" style="left:60px;top:2753px;background:linear-gradient(180deg,#7a4a2c 0%,#9a6a48 45%,#d8c4c8 75%,#e4d6d8 100%)" role="img" aria-label="Worker blowing insulation into an attic"></div>
<div class="abs service-text" style="left:673px;top:2794px">
  <h2>Insulation Services</h2>
  <p>Lorem Ipsum is simply dummy text of the printing and typesetting industry. Lorem Ipsum has been the industry's standard dummy text ever since the 1500s, when an unknown printer took a galley of type and scrambled it to make a type specimen book.</p>
  <p>It is a long established fact that a reader will be distracted by the readable content of a page when looking at its layout. The point of using Lorem Ipsum is that it has a more-or-less normal distribution of letters, as opposed to using 'Content here.</p>
</div>

<section>
  <div class="abs band"></div>
  <svg class="abs band-photo" viewBox="0 0 420 337" role="img" aria-label="Modern home with lit garden pond at dusk">
    <defs><linearGradient id="dusk" x1="0" y1="0" x2="0" y2="1"><stop offset="0" stop-color="#3f6aa0"/><stop offset=".5" stop-color="#b8a58a"/><stop offset="1" stop-color="#2f3a2c"/></linearGradient></defs>
    <polygon points="0,0 350,0 420,168 338,337 0,337" fill="#111"/>
    <polygon points="0,0 340,0 408,168 326,337 0,337" fill="url(#dusk)"/>
  </svg>
  <div class="abs band-text">
    <h2>Holiday lighting</h2>
    <p>Lorem Ipsum is simply dummy text of the printing and typesetting industry. Lorem Ipsum has been the industry's standard dummy text ever since the 1500s, when an unknown printer took a galley of type and scrambled it to make a type specimen book.</p>
    <p>Lorem Ipsum is simply dummy text of the printing and typesetting industry. Lorem Ipsum has been the industry's standard dummy text ever since the 1500s,</p>
  </div>
</section>

<section>
  <h2 class="abs blow-title"><span>BLOW</span></h2>
  <div class="abs card" style="left:168px">
    <svg width="262" height="225" viewBox="0 0 262 225" role="img" aria-label="Worker using a leaf blower in an autumn park"><polygon points="0,0 262,0 262,212 0,225" fill="#2e2e2e"/><polygon points="0,0 262,0 262,206 0,219" fill="#b08a4e"/></svg>
    <h3>Blow In and Removal</h3>
  </div>
  <div class="abs card" style="left:468px">
    <svg width="262" height="225" viewBox="0 0 262 225" role="img" aria-label="Technician performing a blower door test at a doorway"><polygon points="0,0 262,0 262,212 0,225" fill="#2e2e2e"/><polygon points="0,0 262,0 262,206 0,219" fill="#7d7f80"/></svg>
    <h3>Blower Door Tests</h3>
  </div>
  <div class="abs card" style="left:769px">
    <svg width="262" height="225" viewBox="0 0 262 225" role="img" aria-label="Rodent near a trap on a wooden floor"><polygon points="0,0 262,0 262,212 0,225" fill="#2e2e2e"/><polygon points="0,0 262,0 262,206 0,219" fill="#c99a72"/></svg>
    <h3>Rodent Exclusion and Trapping</h3>
  </div>
</section>

<footer>
  <div class="abs footer"></div>
  <div class="abs brand footer-brand"><span class="sq"></span>Hearthwell</div>

  <div class="abs contact" style="left:301px">
    <span class="ico"><svg width="14" height="18" viewBox="0 0 14 18"><path d="M7 0a7 7 0 0 0-7 7c0 5 7 11 7 11s7-6 7-11a7 7 0 0 0-7-7z" fill="#47545e"/><circle cx="7" cy="7" r="2.5" fill="#fff"/></svg></span>
    <span>101- Lorem Ipsum is dummy<br>printing text</span>
  </div>
  <div class="abs contact" style="left:572px;top:4175px">
    <span class="ico"><svg width="16" height="12" viewBox="0 0 16 12"><rect width="16" height="12" rx="1.5" fill="#47545e"/><path d="M1 1l7 6 7-6" stroke="#fff" stroke-width="1.4" fill="none"/></svg></span>
    <span>info@hearthwell.com</span>
  </div>
  <div class="abs contact" style="left:773px;top:4175px">
    <span class="ico"><svg width="16" height="16" viewBox="0 0 24 24"><path d="M6.6 10.8a15 15 0 0 0 6.6 6.6l2.2-2.2a1 1 0 0 1 1-.25 11.4 11.4 0 0 0 3.6.57 1 1 0 0 1 1 1V20a1 1 0 0 1-1 1A17 17 0 0 1 3 4a1 1 0 0 1 1-1h3.5a1 1 0 0 1 1 1c0 1.25.2 2.45.57 3.57a1 1 0 0 1-.25 1z" fill="#47545e"/></svg></span>
    <span>123 456 7890</span>
  </div>

  <div class="abs field" style="left:255px;width:224px">Name*</div>
  <div class="abs field" style="left:487px;width:224px">Email*</div>
  <div class="abs field" style="left:720px;width:224px">Service*</div>
  <div class="abs message">Message</div>
  <div class="abs pill send">SEND</div>

  <div class="abs copyright">©Hearthwell Service - 2021 .All Right Reserved</div>
</footer>

</body>
</html>
```